Tallow Home Buyers

We need a website designed for the a house buying company. It can look and feel similar to a real estate agency, but the messaging is different. Attached in the document below you will see what we are looking for. The main thing we are going for is clean, corporate and approachable. The Logo files are also attached. We want to use the logo and branding throughout the site.

```html
<!DOCTYPE html>
<html lang="en">
<head>
<meta charset="utf-8">
<title>Tallow Home Buyers</title>
<link href="https://fonts.googleapis.com/css2?family=Montserrat:wght@300;400;500;600;700&family=Merriweather:wght@700;900&display=swap" rel="stylesheet">
<style>
:root{
  --green:#6db33f;
  --green-dark:#3e5a20;
  --sage:#7fa593;
  --blue:#174a94;
  --blue-text:#1d4f91;
  --navy:#0c2a55;
  --ink:#1f1f1f;
  --grey-bg:#f5f5f5;
  --grey-mid:#ececec;
  --white:#ffffff;
}
*{box-sizing:border-box;margin:0;padding:0}
html,body{width:1200px;height:5177px;overflow:hidden}
body{font-family:"Montserrat",sans-serif;color:var(--ink);background:var(--white);position:relative}
section,header,footer{position:absolute;left:0;width:1200px;overflow:hidden}
.abs{position:absolute}
.btn{position:absolute;background:var(--green);color:var(--white);font-size:11px;font-weight:600;display:flex;align-items:center;justify-content:center;border-radius:2px}
.center{left:0;width:1200px;text-align:center}
.photo{position:absolute}

/* hero */
.hero{top:0;height:640px}
.hero-photo{inset:0;background:linear-gradient(180deg,#2e74c8 0%,#5c98d8 35%,#c9c0ad 62%,#9a8a6f 80%,#6e6a58 100%)}
.logo-box{left:112px;top:0;width:110px;height:84px;background:var(--white);clip-path:polygon(0 0,100% 0,100% 100%,50% 82%,0 100%);display:flex;flex-direction:column;align-items:center;justify-content:center;padding-bottom:14px}
.logo-name{color:var(--blue-text);font-weight:700;font-size:20px;line-height:1.05;text-align:center;white-space:nowrap}
.logo-sub{color:var(--blue-text);font-weight:700;font-size:8px;letter-spacing:1px;white-space:nowrap;margin-top:2px}
.nav{top:18px;font-size:12px;color:var(--white);white-space:nowrap}
.hero-kicker{left:112px;top:174px;font-family:"Merriweather",serif;font-size:34px;color:var(--white);font-weight:700}
.hero-title{left:112px;top:208px;font-family:"Merriweather",serif;font-size:52px;color:var(--white);font-weight:900}
.hero-sub{left:112px;top:274px;font-size:20px;color:var(--white);font-weight:300}
.hero-input{left:112px;top:322px;width:456px;height:42px;background:var(--white);font-size:11px;padding-left:18px;display:flex;align-items:center;color:#444}

/* selling */
.selling{top:640px;height:743px;background:var(--grey-bg)}
.selling h2{left:108px;top:75px;font-size:32px;font-weight:600}
.selling-lead{left:115px;top:130px;font-size:17px;color:var(--green);line-height:23px;width:620px}
.reason{position:absolute;width:210px}
.reason h4{font-size:11px;color:var(--blue-text);font-weight:600;position:relative;padding-left:24px}
.reason h4::before{content:"";position:absolute;left:0;top:5px;width:4px;height:4px;border-radius:50%;background:var(--blue-text)}
.reason p{font-size:10px;color:#666;line-height:18px;margin-top:8px}
.selling-photo{left:660px;top:63px;width:470px;height:680px;background:linear-gradient(180deg,#f5f5f5 0%,#c6b3a0 22%,#2d3347 50%,#22283a 100%)}

/* benefits */
.benefits{top:1383px;height:437px;background:var(--grey-bg)}
.benefits h2{top:78px;font-size:30px;font-weight:600}
.benefits .sub{top:122px;font-size:17px;color:var(--green)}
.benefit{position:absolute;top:193px;width:200px;text-align:center}
.benefit .ring{width:116px;height:116px;margin:0 auto;border:2px solid var(--blue-text);border-radius:50%;display:flex;align-items:center;justify-content:center}
.benefit p{font-size:14px;color:var(--blue-text);margin-top:28px;font-weight:500}

/* experts */
.experts{top:1820px;height:378px;background:linear-gradient(90deg,#3c5b1f 0%,#4b7126 55%,#5d8c2e 100%)}
.experts h2{left:110px;top:105px;font-size:40px;font-weight:700;color:var(--white);line-height:50px}
.experts-photo{left:795px;top:13px;width:250px;height:365px;background:linear-gradient(180deg,#6e4a3a 0%,#d9a88a 30%,#c4242c 60%,#a51d24 100%)}

/* how it works */
.how{top:2198px;height:502px;background:var(--white)}
.how-photo{left:460px;top:100px;width:740px;height:402px;background:linear-gradient(180deg,#e9e9e9 0%,#9e9e9e 40%,#d8d8d8 75%,#7a7a7a 100%)}
.how h2{top:120px;font-size:30px;font-weight:600}
.steps{left:112px;top:178px;width:976px;height:216px;display:flex}
.step{flex:1;display:flex;flex-direction:column;align-items:center;justify-content:center;color:var(--white);font-size:14px;font-weight:600;text-align:center;line-height:19px;gap:28px}
.step:nth-child(odd){background:var(--green-dark)}
.step:nth-child(even){background:var(--sage)}
.step:last-child{background:var(--green)}

/* video */
.video{top:2700px;height:462px;background:var(--white)}
.video-photo{left:229px;top:46px;width:744px;height:360px;background:linear-gradient(180deg,#3a3a3a 0%,#5a5149 50%,#5b3a26 100%);box-shadow:0 4px 12px rgba(0,0,0,.35)}
.play{left:547px;top:151px}
.video-title{left:229px;width:744px;top:280px;text-align:center;font-size:40px;font-weight:600;color:var(--white)}

/* reviews */
.reviews{top:3162px;height:565px;background:var(--blue);color:var(--white)}
.reviews h2{top:80px;font-size:32px;font-weight:600}
.reviews .sub{top:122px;font-size:17px}
.avatar{position:absolute;top:183px;width:115px;height:115px;border-radius:50%;border:3px solid var(--white)}
.quote{position:absolute;top:320px;width:480px}
.quote h5{font-size:15px;font-weight:500}
.quote p{font-size:11px;line-height:20px;margin-top:6px}
.quote .who{font-size:15px;margin-top:10px}

/* faq */
.faq{top:3727px;height:495px;background:var(--grey-bg)}
.faq h2{top:70px;font-size:32px;font-weight:600}
.faq .sub{top:112px;font-size:17px;color:var(--green)}
.faq-row{position:absolute;left:257px;width:686px;height:44px;background:var(--white);font-size:12px;color:#555;display:flex;align-items:center;justify-content:center}
.faq-row::after{content:"";position:absolute;right:22px;bottom:10px;width:5px;height:5px;border-right:1px solid #999;border-bottom:1px solid #999;transform:rotate(45deg)}

/* contact */
.contact{top:4222px;height:448px;background:var(--grey-mid)}
.contact h2{top:86px;font-size:32px;font-weight:600}
.contact .sub{top:128px;font-size:17px;color:var(--green)}
.field{position:absolute;height:44px;background:var(--white);border:1px solid #ddd;font-size:11px;color:#555;padding-left:18px;display:flex;align-items:center}

/* footer */
.footer{top:4670px;height:507px;background:var(--navy);color:var(--white)}
.footer .label{font-size:14px}
.county{position:absolute;font-size:10px;line-height:26px}
.county li{list-style:none;display:flex}
.county li span{width:28px}
.region{color:var(--green);font-size:11px}
.phone{left:605px;top:112px;font-size:30px;color:var(--green);font-weight:400}
.social{position:absolute;left:605px;display:flex;align-items:center;gap:16px;font-size:10px}
.social i{width:26px;height:26px;border-radius:50%;background:var(--white);display:block}
.foot-logo{right:112px;top:182px;text-align:right;white-space:nowrap}
.foot-logo .name{font-size:34px;font-weight:700;line-height:36px}
.foot-logo .tag{font-size:12px;font-weight:700;letter-spacing:3px}
.copy{right:112px;top:258px;font-size:11px;text-align:right;line-height:24px;white-space:nowrap}
.copy b{color:var(--green);font-weight:400}
.badge{left:971px;top:301px;width:117px;height:42px;background:#1f5c8a;border-radius:3px}
</style>
</head>
<body>

<header class="hero">
  <div class="photo hero-photo" role="img" aria-label="Street of two-storey suburban homes with tiled roofs under a blue sky"></div>
  <div class="abs logo-box"><div class="logo-name">Tallow</div><div class="logo-sub">HOME BUYERS</div></div>
  <nav>
    <span class="abs nav" style="left:277px">Home</span>
    <span class="abs nav" style="left:338px">Why Tallow Home Buyers</span>
    <span class="abs nav" style="left:512px">How It Works</span>
    <span class="abs nav" style="left:619px">Reasons to Sell</span>
    <span class="abs nav" style="left:738px">Locations</span>
    <span class="abs nav" style="left:824px">FAQ</span>
    <span class="abs nav" style="left:874px">Contact</span>
    <span class="abs nav" style="left:966px;top:14px;display:flex;align-items:center;gap:6px">
      <svg width="14" height="14" viewBox="0 0 24 24"><path d="M6.6 10.8a15 15 0 006.6 6.6l2.2-2.2a1 1 0 011-.25 11.4 11.4 0 003.6.57 1 1 0 011 1V20a1 1 0 01-1 1A17 17 0 013 4a1 1 0 011-1h3.5a1 1 0 011 1 11.4 11.4 0 00.57 3.6 1 1 0 01-.25 1z" fill="#fff"/></svg>
      (555) 214-7730</span>
  </nav>
  <div class="abs hero-kicker">We Buy Homes From People</div>
  <div class="abs hero-title">IN NO TIME!</div>
  <div class="abs hero-sub">Get Your Cash Offer Today.</div>
  <div class="abs hero-input">Enter Your Street Address</div>
  <div class="btn" style="left:563px;top:326px;width:131px;height:34px">Get Your Free Offer</div>
</header>

<section class="selling">
  <h2 class="abs">Thinking of Selling?</h2>
  <p class="abs selling-lead">No matter your situation, we will buy your home.<br>No need to worry about the condition of the house either<br>- we’ll make this a stress-free process and get you cash quickly.</p>
  <div class="reason" style="left:114px;top:246px"><h4>Retirement</h4></div>
  <div class="reason" style="left:114px;top:278px"><h4>Divorce</h4></div>
  <div class="reason" style="left:114px;top:395px"><h4>Bad Mortgage</h4><p>Selling your home is a great way to get out of your current mortgage quick.</p></div>
  <div class="reason" style="left:114px;top:514px"><h4>Divorce</h4></div>
  <div class="reason" style="left:345px;top:246px"><h4>Downsizing or Upsizing</h4></div>
  <div class="reason" style="left:345px;top:278px"><h4>Inheritance</h4><p>Have you inherited a home and you don’t want to worry about the headache that comes with it? Sell it to the Tallow Home Experts!</p></div>
  <div class="reason" style="left:345px;top:395px"><h4>Massive Repairs</h4><p>Is your home too much to manage? No problem; our team is happy to take it off your hands.</p></div>
  <div class="reason" style="left:345px;top:514px"><h4>Moving</h4><p>Sometimes you just want to move and that’s okay too! Let us help you get into your dream home.</p></div>
  <div class="btn" style="left:112px;top:644px;width:182px;height:36px">More Reasons to Sell</div>
  <div class="photo selling-photo" role="img" aria-label="Smiling bearded man in a blazer presenting a green house shape with his hand"></div>
</section>

<section class="benefits">
  <h2 class="abs center">Reasons People Work With Tallow</h2>
  <p class="abs center sub">Benefits of working with us over a realtor.</p>
  <div class="benefit" style="left:125px"><div class="ring">
    <svg width="56" height="56" viewBox="0 0 56 56" fill="none" stroke="#6db33f" stroke-width="2"><circle cx="30" cy="31" r="18"/><path d="M30 31l8-8M26 9h8M30 9v4M4 26h10M6 32h8M8 38h6"/></svg></div><p>Quick Turnaround</p></div>
  <div class="benefit" style="left:374px"><div class="ring">
    <svg width="56" height="56" viewBox="0 0 56 56" fill="none" stroke="#6db33f" stroke-width="2"><circle cx="30" cy="20" r="12"/><path d="M30 13v14M34 16h-6a2.5 2.5 0 000 5h4a2.5 2.5 0 010 5h-6M6 40h12l8 4h14l8-6"/></svg></div><p>Zero Fees</p></div>
  <div class="benefit" style="left:624px"><div class="ring">
    <svg width="56" height="56" viewBox="0 0 56 56" fill="none" stroke="#6db33f" stroke-width="2"><path d="M20 36a13 13 0 1116 0v6H20z M22 47h12M28 3v5M10 10l4 4M46 10l-4 4"/></svg></div><p>Stress &amp; Hassle Free</p></div>
  <div class="benefit" style="left:873px"><div class="ring">
    <svg width="56" height="56" viewBox="0 0 56 56" fill="none" stroke="#6db33f" stroke-width="2"><rect x="12" y="10" width="30" height="36" rx="2"/><circle cx="27" cy="24" r="6"/><path d="M8 44h20l6-6h10"/></svg></div><p>Cold Hard Cash Fast</p></div>
</section>

<section class="experts">
  <h2 class="abs">We’re the experts<br>you turn to every time.</h2>
  <div class="btn" style="left:112px;top:228px;width:150px;height:34px">Get Started</div>
  <div class="photo experts-photo" role="img" aria-label="Smiling woman in a red blazer with arms crossed"></div>
</section>

<section class="how">
  <div class="photo how-photo" role="img" aria-label="Black and white photo of a house facade with porch and shutters"></div>
  <h2 class="abs center">How It Works</h2>
  <div class="abs steps">
    <div class="step"><svg width="44" height="44" viewBox="0 0 24 24" fill="none" stroke="#fff" stroke-width="1.2"><path d="M6.6 10.8a15 15 0 006.6 6.6l2.2-2.2a1 1 0 011-.25 11.4 11.4 0 003.6.57 1 1 0 011 1V20a1 1 0 01-1 1A17 17 0 013 4a1 1 0 011-1h3.5a1 1 0 011 1 11.4 11.4 0 00.57 3.6 1 1 0 01-.25 1z"/></svg><span>Call or<br>Email Us</span></div>
    <div class="step"><svg width="44" height="44" viewBox="0 0 24 24" fill="none" stroke="#fff" stroke-width="1.2"><path d="M4 14v-2a8 8 0 0116 0v2"/><rect x="3" y="13" width="4" height="6" rx="1"/><rect x="17" y="13" width="4" height="6" rx="1"/><path d="M19 19c0 2-3 3-6 3"/></svg><span>Speak to a<br>Tallow Expert</span></div>
    <div class="step"><svg width="44" height="44" viewBox="0 0 24 24" fill="none" stroke="#fff" stroke-width="1.2"><rect x="3" y="5" width="18" height="16" rx="1"/><path d="M3 9h18M8 3v4M16 3v4"/><circle cx="8" cy="13" r="1"/><circle cx="12" cy="13" r="1"/><circle cx="16" cy="13" r="1"/><circle cx="8" cy="17" r="1"/><circle cx="12" cy="17" r="1"/></svg><span>Schedule a Quick<br>Walk-Through</span></div>
    <div class="step"><svg width="44" height="44" viewBox="0 0 24 24" fill="none" stroke="#fff" stroke-width="1.2"><circle cx="14" cy="8" r="6"/><path d="M11 11l6-6M12 6h.01M16 10h.01M2 18h6l4 2h6l4-3"/></svg><span>Receive a<br>Cash Offer</span></div>
    <div class="step"><svg width="44" height="44" viewBox="0 0 24 24" fill="none" stroke="#fff" stroke-width="1.2"><rect x="6" y="4" width="14" height="8" rx="1"/><circle cx="13" cy="8" r="2"/><path d="M2 17h6l4 2h6l4-3"/></svg><span>Get Paid</span></div>
  </div>
</section>

<section class="video">
  <div class="photo video-photo" role="img" aria-label="Two-storey house on a lawn under a cloudy sky, video still"></div>
  <svg class="abs play" width="106" height="106" viewBox="0 0 106 106"><circle cx="53" cy="53" r="51" fill="none" stroke="#fff" stroke-width="2"/><path d="M44 38l24 15-24 15z" fill="#e3262b"/></svg>
  <div class="abs video-title">Close as Fast as 7 Days!</div>
</section>

<section class="reviews">
  <h2 class="abs center">Reviews</h2>
  <p class="abs center sub">Hear from satisfied sellers</p>
  <div class="avatar" style="left:112px;background:linear-gradient(180deg,#e2d3c0,#c99f78)" role="img" aria-label="Portrait of a smiling blonde woman"></div>
  <div class="avatar" style="left:973px;background:linear-gradient(180deg,#c8d2dc,#2a3446)" role="img" aria-label="Portrait of a smiling man in a suit"></div>
  <div class="quote" style="left:112px"><h5>“Smooth, easy, fast.”</h5><p>I was hesitant of the whole deal, because it seemed too easy. And now that I’m at the final sale, if Dale tells you he’s doing it, he’s doing it. It’s that simple.”</p><p class="who">~ Megan</p></div>
  <div class="quote" style="left:608px;text-align:right"><h5>“Really Good”</h5><p>Various versions have evolved over the years, sometimes by accident, sometimes on purpose (injected humour and the like).”</p><p class="who">~ Owen Marsh</p></div>
  <svg class="abs" style="left:572px;top:424px" width="56" height="20" viewBox="0 0 56 20" fill="none" stroke-width="2"><path d="M12 3l-7 7 7 7" stroke="#6db33f"/><path d="M44 3l7 7-7 7" stroke="#fff"/></svg>
  <div class="btn" style="left:535px;top:484px;width:130px;height:36px">See All Stories</div>
</section>

<section class="faq">
  <h2 class="abs center">Questions?</h2>
  <p class="abs center sub">We have the answers.</p>
  <div class="faq-row" style="top:170px">How fast does this work?</div>
  <div class="faq-row" style="top:229px">What are your fees?</div>
  <div class="faq-row" style="top:287px">What if my home is not in good shape?</div>
  <div class="btn" style="left:535px;top:367px;width:130px;height:36px">More FAQs</div>
</section>

<section class="contact">
  <h2 class="abs center">Contact Us</h2>
  <p class="abs center sub">Speak with a Tallow Expert today.</p>
  <div class="field" style="left:112px;top:186px;width:234px">Full Name</div>
  <div class="field" style="left:358px;top:186px;width:235px">Phone</div>
  <div class="field" style="left:605px;top:186px;width:235px">Email</div>
  <div class="field" style="left:852px;top:186px;width:236px">Street Address</div>
  <div class="field" style="left:112px;top:246px;width:318px">City</div>
  <div class="field" style="left:442px;top:246px;width:316px">State</div>
  <div class="field" style="left:770px;top:246px;width:318px">Zip</div>
  <div class="btn" style="left:535px;top:314px;width:130px;height:36px">Get a Cash Offer</div>
</section>

<footer class="footer">
  <div class="abs label" style="left:112px;top:80px">Find Our Location</div>
  <ul class="county" style="left:112px;top:114px">
    <li class="region"><span>A.</span>Southern California</li>
    <li><span>i.</span>Los Angeles County</li>
    <li><span>ii.</span>Orange County</li>
    <li><span>iii.</span>San Bernardino County</li>
    <li><span>iv.</span>Riverside County</li>
  </ul>
  <ul class="county" style="left:318px;top:114px">
    <li class="region"><span>B.</span>Northern California</li>
    <li><span>i.</span>Contra Costa County</li>
    <li><span>ii.</span>Alameda County</li>
    <li><span>iii.</span>Stanislaus County</li>
    <li><span>iv.</span>Sonoma County</li>
    <li><span>v.</span>Napa County</li>
    <li><span>vi.</span>Solona County</li>
    <li><span>vii.</span>Santa Clara County</li>
    <li><span>viii.</span>Merced County</li>
    <li><span>ix.</span>Sacramento County</li>
    <li><span>x.</span>San Joaquin County</li>
    <li><span>xi.</span>San Mateo County</li>
  </ul>
  <div class="abs label" style="left:605px;top:88px">Call Us :</div>
  <div class="abs phone">(555) 214-7730</div>
  <div class="abs label" style="left:605px;top:202px">Follow Us</div>
  <div class="social" style="top:240px"><i></i>Video Channel</div>
  <div class="social" style="top:278px"><i></i>Community Page</div>
  <div class="social" style="top:316px"><i></i>Photo Feed</div>
  <div class="abs foot-logo"><div class="name">Tallow</div><div class="tag">HOME BUYERS</div></div>
  <div class="abs copy">Copyright©2019 <b>Tallow Home Buyers.</b><br>All Rights Reserved.</div>
  <div class="abs badge"></div>
</footer>

</body>
</html>
```